Carte d'affaire bilingue

Nous avons besoin d'une carte d'affaire pour notre entreprise spécialisée en vente et achat de terrain. Nous sommes une agence immobilière et nous voulons une carte avec le recto en Français et le verso en anglais. Nous voulons une image sobre et épurée. Nous avons de la clientèle internationale et nous voulons une carte très professionnelle mais qui se démarque. Nous voulons cibler une clientèle commerciale, industrielle, contracteurs et promoteurs immobiliers.
Updates

Hi everybody, we saw all your conception and we are approching of what we like but the "WOW" is missing.

We love the little sign to specify (phone or email) but we can put them in a square to make like our logo, we love also dark gray not lite gray, we also love the stainless lines. In our logo you can see a little sign +. For us is signyfy " Always further" so if you can put many little +++++ in the conception somewhere very discret it will be appreciate. We also like a kind of round that make a magnyfying glass, because we search land we found opportunity.

Thank you

Reason: I ask different things in the last day but no one do what i am asking for. For the conception # 3016702 that we love we ask changes.

We like simplicity, urban design, corporate, international. The card must have one side in french and the other side in english. We like dark gray,silver, and a little bit of green.

Target Market(s)

Investors, developers, construction builders, etc...

Font styles to use
Serif
Sans Serif

Requirements
Must have
• logo
La mention: Agence immobilière (Francais) / Real Estate Agency (anglais)
Sous le nom: Courtier immobilier agréé (Français) / Real Estate Broker

```html
<!DOCTYPE html>
<html lang="fr">
<head>
<meta charset="utf-8">
<title>Le Repère Foncier – Carte d'affaires / Business card</title>
<link href="https://fonts.googleapis.com/css2?family=Alegreya+SC:wght@400;500&display=swap" rel="stylesheet">
<style>
  :root {
    --backdrop: #d9d9d9;
    --card: #f7f7f7;
    --ink: #1e1e1e;
    --ink-soft: #3a3a3a;
    --green: #1f8a3a;
    --silver: #9a9a9a;
    --card-shadow: rgba(0,0,0,0.18);
  }
  * { margin: 0; padding: 0; box-sizing: border-box; }
  html, body { width: 1200px; height: 800px; overflow: hidden; }
  body {
    background: var(--backdrop);
    font-family: "Alegreya SC", Georgia, serif;
    color: var(--ink);
    position: relative;
  }
  .card {
    position: absolute;
    top: 257px;
    width: 500px;
    height: 286px;
    background: var(--card);
    box-shadow: 0 6px 18px var(--card-shadow);
  }
  .card--fr { left: 70px; }
  .card--en { left: 630px; }

  .brand {
    position: absolute;
    top: 32px;
    right: 32px;
    display: flex;
    align-items: center;
    gap: 10px;
  }
  .brand__square {
    width: 22px;
    height: 22px;
    background: var(--green);
    flex: none;
  }
  .brand__name {
    font-size: 26px;
    font-weight: 500;
    color: var(--ink-soft);
    letter-spacing: 0.02em;
    line-height: 1;
    white-space: nowrap;
  }
  .agency {
    position: absolute;
    top: 68px;
    right: 32px;
    font-size: 12px;
    letter-spacing: 0.06em;
    color: var(--ink-soft);
  }
  .rule {
    position: absolute;
    top: 90px;
    right: 32px;
    width: 220px;
    height: 1px;
    background: var(--silver);
  }
  .person {
    position: absolute;
    left: 32px;
    top: 108px;
  }
  .person__name {
    font-size: 24px;
    font-weight: 500;
    letter-spacing: 0.02em;
    line-height: 1.2;
  }
  .person__role {
    font-size: 12px;
    letter-spacing: 0.05em;
    color: var(--ink-soft);
    line-height: 1.4;
  }
  .web {
    position: absolute;
    right: 32px;
    top: 186px;
    text-align: right;
    font-size: 11px;
    line-height: 1.45;
    letter-spacing: 0.03em;
  }
  .contact {
    position: absolute;
    left: 32px;
    right: 32px;
    bottom: 24px;
    font-size: 11px;
    letter-spacing: 0.03em;
    line-height: 1.6;
    white-space: nowrap;
  }
  .contact__label { color: var(--green); font-weight: 500; }
</style>
</head>
<body>
  <section class="card card--fr" aria-label="Recto, français">
    <div class="brand">
      <span class="brand__square"></span>
      <span class="brand__name">Le Repère Foncier</span>
    </div>
    <p class="agency">Agence immobilière</p>
    <div class="rule"></div>

    <div class="person">
      <p class="person__name">Martine Lavoie</p>
      <p class="person__role">Courtier immobilier agréé D.A.</p>
      <p class="person__role">Vice-présidente</p>
    </div>

    <div class="web">
      <p>m.lavoie@reperefoncier.com</p>
      <p>www.reperefoncier.com</p>
    </div>

    <div class="contact">
      <p><span class="contact__label">T.</span> 514 555 0142 &nbsp;<span class="contact__label">F.</span> 450 555 0187 &nbsp;<span class="contact__label">C.</span> 514 555 0163 &nbsp;<span class="contact__label">SF</span> 1 866 555 0100</p>
      <p>120 Rue des Érables, 2e, Laval, QC, H7A 1B2</p>
    </div>
  </section>

  <section class="card card--en" lang="en" aria-label="Back, English">
    <div class="brand">
      <span class="brand__square"></span>
      <span class="brand__name">Le Repère Foncier</span>
    </div>
    <p class="agency">Real Estate Agency</p>
    <div class="rule"></div>

    <div class="person">
      <p class="person__name">Martine Lavoie</p>
      <p class="person__role">Real Estate Broker</p>
      <p class="person__role">Vice-President</p>
    </div>

    <div class="web">
      <p>m.lavoie@reperefoncier.com</p>
      <p>www.reperefoncier.com</p>
    </div>

    <div class="contact">
      <p><span class="contact__label">T.</span> 514 555 0142 &nbsp;<span class="contact__label">F.</span> 450 555 0187 &nbsp;<span class="contact__label">C.</span> 514 555 0163 &nbsp;<span class="contact__label">TF</span> 1 866 555 0100</p>
      <p>120 Rue des Érables, 2nd floor, Laval, QC, H7A 1B2</p>
    </div>
  </section>
</body>
</html>
```